transgender support group needs innovative business card and logo

we are a transgender support group looking for a new logo and business card. I would like to include a Dora Vell head (our logo), over top of, or somehow incorporate a rainbow (an LGBT symbol) arcing over the lower left third of the card, allowing for the text on the remaining part. Other designs are welcome, as this is just some guidance to start. I would like "MERIDAN" to possibly be larger the the "learning society", and under that, I would like "a transgender resource" We also need room for the address, website and phone number. A bit larger, would need to be a spot for a name and title.
Meridian Learning Society, 412 Birchwood Hollow rd. Ashby vt05342 suite 352. phone 802 555 0147 contact person Brenna Calloway, president

```html
<!DOCTYPE html>
<html lang="en">
<head>
<meta charset="utf-8">
<title>Meridian Learning Society – Business Card</title>
<link rel="stylesheet" href="https://fonts.googleapis.com/css2?family=Itim&display=swap">
<style>
  :root {
    --backdrop: #8f8f8f;
    --card-light: #8299b0;
    --card-dark: #46587b;
    --ink: #ffffff;
    --portrait-tone: rgba(255,255,255,0.2);
    --stripe-violet: #e68af0;
    --stripe-blue: #a9c1f5;
    --stripe-green: #9ee8a8;
    --stripe-yellow: #f6f19a;
    --stripe-orange: #f7c997;
    --stripe-red: #f88f8b;
  }
  * { box-sizing: border-box; margin: 0; padding: 0; }
  html, body {
    width: 1200px; height: 1000px; overflow: hidden;
    background: var(--backdrop);
  }
  .stage {
    width: 1200px; height: 1000px;
    display: flex; align-items: center; justify-content: center;
  }
  .business-card {
    position: relative;
    width: 500px; height: 875px;
    background: linear-gradient(160deg, var(--card-light) 0%, var(--card-dark) 100%);
    font-family: "Itim", "Comic Sans MS", sans-serif;
    color: var(--ink);
    overflow: hidden;
  }
  .portrait-area {
    position: absolute; left: 150px; top: 50px;
    width: 210px; height: 200px;
    border-radius: 50%;
    background: var(--portrait-tone);
  }
  .logo-block {
    position: absolute; left: 48px; top: 275px; width: 404px;
  }
  .logo-name {
    font-size: 38px; line-height: 1.05;
  }
  .logo-tagline {
    margin-top: 8px;
    font-size: 20px; letter-spacing: 0.5px;
  }
  .contact-person {
    position: absolute; left: 48px; top: 420px; width: 404px;
  }
  .person-name { font-size: 44px; line-height: 1.1; }
  .person-title { font-size: 26px; margin-top: 2px; padding-left: 4px; }
  .rainbow-band {
    position: absolute; left: 0; right: 0;
    display: flex;
  }
  .rainbow-band span { flex: 1; }
  .rainbow-band--middle { top: 560px; height: 92px; }
  .rainbow-band--bottom { top: 795px; height: 80px; }
  .rainbow-band .violet { background: var(--stripe-violet); }
  .rainbow-band .blue   { background: var(--stripe-blue); }
  .rainbow-band .green  { background: var(--stripe-green); }
  .rainbow-band .yellow { background: var(--stripe-yellow); }
  .rainbow-band .orange { background: var(--stripe-orange); }
  .rainbow-band .red    { background: var(--stripe-red); }
  .address {
    position: absolute; left: 40px; top: 664px; width: 430px;
    font-size: 26px; line-height: 1.12; font-style: normal;
  }
</style>
</head>
<body>
<main class="stage">
  <section class="business-card">
    <div class="portrait-area" role="img" aria-label="Line-art portrait of the society's emblem figure"></div>

    <div class="logo-block">
      <div class="logo-name">Meridian Learning Society</div>
      <div class="logo-tagline">a transgender resource</div>
    </div>

    <div class="contact-person">
      <div class="person-name">Brenna Calloway</div>
      <div class="person-title">President</div>
    </div>

    <div class="rainbow-band rainbow-band--middle" aria-hidden="true">
      <span class="violet"></span><span class="blue"></span><span class="green"></span><span class="yellow"></span><span class="orange"></span><span class="red"></span>
    </div>

    <address class="address">
      Meridian Learning Society,<br>
      412 Birchwood Hollow rd.<br>
      Ashby vt05342 suite 352.<br>
      phone 802 555 0147
    </address>

    <div class="rainbow-band rainbow-band--bottom" aria-hidden="true">
      <span class="violet"></span><span class="blue"></span><span class="green"></span><span class="yellow"></span><span class="orange"></span><span class="red"></span>
    </div>
  </section>
</main>
</body>
</html>
```